Want to fly? Flight school needs a roll up

Hello designers

We are a small aviation club with around 100 members. We love flying and therefore offer free flight lessons for young people at our glider flight school.
The young people only have to pay a flat rate of €300 for the aircraft until their first solo flight.
To advertise the flight school we now need a roll up banner measuring 85cm x 200cm. You can find the data sheet for the banner in the appendix.
Content of the roll up banner:
Advertising for our flight school so that we can attract new members
The banner should be designed in our club colors blue/white
The banner is aimed at all people who want to get a glider license
A great offer for young people up to the age of 25 should be placed on the banner with a reference to the text “Offer only applies to people up to the age of 25. Included in the flat rate of €300 is training on the glider up to the first "solo flight"
The banner is intended to advertise training with a glider. Therefore the wish would be for a glider to be depicted

Here is a link to our current homepage

https://www.lsg-tarnhofen.de/

https://www.vidoplex.example/watch?v=K8p2Qz4LmXc

Target Market(s)

Young people from 14 years to 30 years

Colors
0054AA
0677BA
7BADD7
CADEEF
E8F1F8

Requirements
Nice to have
• Glider / club logo
Should not have
• Too much text

```html
<!DOCTYPE html>
<html lang="en">
<head>
<meta charset="utf-8">
<title>Free Flight Lessons – Roll-up Banner</title>
<link rel="stylesheet" href="https://fonts.googleapis.com/css2?family=Bebas+Neue&family=Poppins:wght@600;700;800;900&display=swap">
<style>
  :root {
    --club-blue: #0b10a3;
    --club-navy: #141a7a;
    --ink: #2e2e2e;
    --paper: #ffffff;
    --divider: rgba(0, 0, 0, 0.16);
    --grass-light: #8fb35a;
    --grass-dark: #4f7a2c;
    --sky: #dfe6ea;
  }
  * { margin: 0; padding: 0; box-sizing: border-box; }
  html, body { width: 1200px; height: 4000px; overflow: hidden; background: var(--paper); }
  .banner { position: relative; width: 1200px; height: 4000px; background: var(--paper); overflow: hidden; }
  .banner__shapes { position: absolute; inset: 0; }
  .club-mark {
    position: absolute; left: 0; right: 0; top: 150px;
    display: flex; flex-direction: column; align-items: center; gap: 22px;
  }
  .club-mark__disc {
    width: 330px; height: 330px; border-radius: 50%;
    background: var(--paper);
  }
  .club-mark__name {
    font-family: "Poppins", sans-serif; font-weight: 700; font-size: 34px;
    color: var(--club-blue); letter-spacing: 1px;
  }
  .offer { position: absolute; left: 0; right: 0; text-align: center; }
  .headline-free {
    top: 750px; font-family: "Poppins", sans-serif; font-weight: 900;
    font-size: 230px; line-height: 1; color: var(--club-blue); letter-spacing: -2px;
  }
  .display {
    font-family: "Bebas Neue", sans-serif; color: var(--club-blue); line-height: 1;
  }
  .headline-lessons { top: 985px; font-size: 170px; }
  .body-copy {
    font-family: "Poppins", sans-serif; font-weight: 700; color: var(--ink);
    font-size: 78px; line-height: 1.08;
  }
  .copy-age { top: 1170px; }
  .headline-age { top: 1380px; font-size: 200px; }
  .divider {
    position: absolute; left: 20px; right: 120px; height: 40px;
    background: radial-gradient(ellipse at 50% 0%, var(--divider), transparent 70%);
  }
  .divider--one { top: 1610px; }
  .copy-rate { top: 1680px; }
  .headline-price { top: 1870px; font-size: 200px; }
  .divider--two { top: 2090px; }
  .copy-training { top: 2150px; font-size: 74px; }
  .headline-solo { top: 2340px; font-size: 200px; }
  .glider-photo { position: absolute; inset: 0; }
  .web-pill {
    position: absolute; left: 72px; right: 60px; top: 3730px; height: 150px;
    border-radius: 75px; background: var(--club-navy);
    display: flex; align-items: center; justify-content: center;
    font-family: "Bebas Neue", sans-serif; font-size: 132px; color: var(--paper);
    letter-spacing: 1px; padding-top: 10px;
  }
</style>
</head>
<body>
  <main class="banner">
    <svg class="banner__shapes" width="1200" height="4000" viewBox="0 0 1200 4000" aria-hidden="true">
      <defs>
        <linearGradient id="photoTones" x1="0" y1="0" x2="0" y2="1">
          <stop offset="0" stop-color="#dfe6ea"/>
          <stop offset="0.35" stop-color="#f4f6f6"/>
          <stop offset="0.55" stop-color="#8fb35a"/>
          <stop offset="1" stop-color="#4f7a2c"/>
        </linearGradient>
      </defs>
      <path class="top-band" d="M0 0 H1200 V90 Q600 620 0 90 Z" fill="var(--club-blue)"/>
      <path class="top-band__line" d="M10 150 Q600 690 1190 150" fill="none" stroke="var(--club-blue)" stroke-width="8"/>
    </svg>

    <svg class="glider-photo" width="1200" height="4000" viewBox="0 0 1200 4000" role="img" aria-label="Photo of a white two-seat glider parked on a grass airfield with club members beside it">
      <path d="M0 3620 Q600 2150 1200 3620 V4000 H0 Z" fill="url(#photoTones)"/>
      <path d="M0 3620 Q600 2150 1200 3620" fill="none" stroke="var(--club-blue)" stroke-width="18"/>
    </svg>

    <div class="club-mark">
      <div class="club-mark__disc"></div>
      <p class="club-mark__name">Luftsportgruppe Tarnhofen e.V.</p>
    </div>

    <h1 class="offer headline-free">FREE</h1>
    <h2 class="offer display headline-lessons">FLIGHT LESSONS</h2>
    <p class="offer body-copy copy-age">Offer only applies<br>to people up&nbsp; to the</p>
    <p class="offer display headline-age">AGE OF 25</p>
    <div class="divider divider--one"></div>
    <p class="offer body-copy copy-rate">Included in the<br>flat rate of</p>
    <p class="offer display headline-price">€300</p>
    <div class="divider divider--two"></div>
    <p class="offer body-copy copy-training">Is training on the glider<br>up to the</p>
    <p class="offer display headline-solo">FIRST SOLO FLIGHT</p>

    <p class="web-pill">www.lsg-tarnhofen.de</p>
  </main>
</body>
</html>
```